Business Card Design

I need a Business Card that will catch the attention that will not get thrown in a Drawer. I have 23 companies I use for Auto, Home, Life, and Business Insurance. I make sure that people have the best coverage for the $ spent.

Industry/Entity Type

Business

Contact Information for Business Card

Torvin Insurance Agency, Inc., Derek Halloway, 4735 West Fallow Lane Ashmere, Iowa 52913 555-287-6194, www.torvinagency-example.com, Facebook, LinkedIn, Google+

```html
<!DOCTYPE html>
<html lang="en">
<head>
<meta charset="utf-8">
<title>Torvin Insurance Agency – Business Card</title>
<link rel="stylesheet" href="https://fonts.googleapis.com/css2?family=Bebas+Neue&family=Cinzel:wght@400&display=swap">
<style>
  :root {
    --band: #3b3531;
    --paper: #ffffff;
    --ink-brown: #7a4a25;
    --frame: #5a4c44;
    --chip: #6b5f57;
    --light-text: #ffffff;
  }
  html, body {
    margin: 0;
    padding: 0;
    width: 1200px;
    height: 695px;
    overflow: hidden;
    background: var(--paper);
  }
  .card {
    position: relative;
    width: 1200px;
    height: 695px;
    background: var(--paper);
    overflow: hidden;
  }
  .header-band {
    position: absolute;
    left: 0; top: 0;
    width: 1200px;
    height: 189px;
    background: var(--band);
  }
  .agency-name {
    position: absolute;
    left: 0; top: 58px;
    width: 1276px;
    margin: 0;
    text-align: center;
    font-family: "Cinzel", serif;
    font-weight: 400;
    font-size: 51px;
    letter-spacing: 3px;
    color: var(--light-text);
    line-height: 1;
  }
  .monogram-box {
    position: absolute;
    left: 555px; top: 138px;
    width: 95px; height: 95px;
  }
  .agent-name {
    position: absolute;
    left: 0; top: 283px;
    width: 1210px;
    margin: 0;
    text-align: center;
    font-family: "Bebas Neue", sans-serif;
    font-weight: 400;
    font-size: 100px;
    letter-spacing: 7px;
    color: var(--ink-brown);
    line-height: 1;
  }
  .address {
    position: absolute;
    left: 0; top: 424px;
    width: 1204px;
    margin: 0;
    text-align: center;
    font-family: "Bebas Neue", sans-serif;
    font-style: normal;
    font-size: 49px;
    letter-spacing: 2px;
    line-height: 59px;
    color: var(--ink-brown);
  }
  .footer-band {
    position: absolute;
    left: 0; top: 584px;
    width: 1200px;
    height: 64px;
    background: var(--band);
  }
  .phone, .website {
    position: absolute;
    margin: 0;
    font-family: "Bebas Neue", sans-serif;
    line-height: 1;
    color: var(--light-text);
  }
  .phone { left: 63px; top: 595px; font-size: 49px; letter-spacing: 2px; }
  .website { left: 417px; top: 598px; font-size: 44px; letter-spacing: 1px; }
  .social-links {
    position: absolute;
    left: 957px; top: 592px;
    width: 180px; height: 50px;
  }
</style>
</head>
<body>
  <main class="card">
    <div class="header-band"></div>
    <h1 class="agency-name">Torvin Insurance Agency, Inc.</h1>

    <svg class="monogram-box" viewBox="0 0 95 95" aria-hidden="true">
      <rect x="2.5" y="2.5" width="90" height="90" rx="5" fill="#ffffff" stroke="var(--frame)" stroke-width="5"/>
    </svg>

    <h2 class="agent-name">Derek Halloway</h2>

    <address class="address">
      4735 West Fallow Lane<br>
      Ashmere, Iowa 52913
    </address>

    <div class="footer-band"></div>
    <p class="phone">555-287-6194</p>
    <p class="website">www.torvinagency-example.com</p>

    <svg class="social-links" viewBox="0 0 180 50" aria-label="Social media links">
      <rect x="0" y="0" width="50" height="50" rx="4" fill="var(--chip)"/>
      <rect x="64" y="0" width="50" height="50" rx="4" fill="var(--chip)"/>
      <rect x="128" y="0" width="50" height="50" rx="4" fill="var(--chip)"/>
    </svg>
  </main>
</body>
</html>
```